Business card design

We need a business card design for our law firm in Australia. Our firm's name is "KD LORN Lawyers & Notary". Our slogan is "Every Matter Handled with Steady Care".

We would like to use the burgundy tone.

Industry/Entity Type

Law Firm

Contact Information for Business Card

Clara Bexley
Solicitor
Notary Public (Qld & Vic)
Migration Agent
LLB, LLM, Grad Dip in LP, Grad Dip in NP
RMA 0853162

Office Address: 24/6 Tolvern Road Marleigh QLD 4287 Australia
Postal Address: P O Box 61 Marleigh QLD 4287 Australia
Telephone: 1300 274 563
Facsimile: 1300 274 569
International Telephone: +617 3956 2740
International Facsimile: +617 3871 6025
Email: clara.bexley@kdlornlegal.example
Web: www.kdlornlegal.example

```html
<!DOCTYPE html>
<html lang="en">
<head>
<meta charset="utf-8">
<title>KD LORN Lawyers &amp; Notary — Business Card</title>
<link rel="stylesheet" href="https://fonts.googleapis.com/css2?family=Arimo:wght@700&family=Source+Sans+3:wght@400;500;600&display=swap">
<style>
  :root {
    --page: #ffffff;
    --card-centre: #ffffff;
    --card-mid: #fbf3f2;
    --card-edge: #f1dcd9;
    --accent: #7a1f2e;
    --ink: #2e1a16;
    --wave: rgba(255, 255, 255, 0.55);
  }
  html, body {
    margin: 0;
    padding: 0;
    width: 1200px;
    height: 900px;
    overflow: hidden;
    background: var(--page);
  }
  .canvas {
    position: relative;
    width: 1200px;
    height: 900px;
  }
  .card {
    position: absolute;
    overflow: hidden;
    background: radial-gradient(ellipse at 50% 50%, var(--card-centre) 0%, var(--card-centre) 30%, var(--card-edge) 100%);
  }
  .card--front { left: 322px; top: 62px; width: 592px; height: 343px; }
  .card--back {
    left: 324px; top: 461px; width: 594px; height: 342px;
    background: radial-gradient(ellipse at 60% 70%, var(--card-centre) 0%, var(--card-mid) 40%, var(--card-edge) 100%);
  }
  .wave { position: absolute; left: 0; top: 0; width: 100%; height: 100%; }

  .brand { position: absolute; }
  .brand__name {
    margin: 0;
    font-family: "Arimo", Arial, sans-serif;
    font-weight: 700;
    font-size: 21px;
    letter-spacing: 0.2px;
    color: var(--accent);
    white-space: nowrap;
  }
  .brand__slogan {
    margin: 4px 0 0 2px;
    font-family: "Source Sans 3", "Myriad Pro", sans-serif;
    font-weight: 400;
    font-size: 14px;
    color: var(--ink);
    white-space: nowrap;
  }
  .brand__dot {
    position: absolute;
    border-radius: 50%;
    background: var(--accent);
  }
  .card--front .brand { left: 116px; top: 150px; }
  .card--front .brand__dot { left: 406px; top: 134px; width: 66px; height: 66px; }
  .card--back .brand { left: 33px; top: 44px; }
  .card--back .brand__dot { left: 324px; top: 26px; width: 68px; height: 68px; }

  .contact {
    position: absolute;
    left: 33px;
    top: 122px;
    margin: 0;
    font-style: normal;
    font-family: "Source Sans 3", "Myriad Pro", sans-serif;
    font-size: 13px;
    line-height: 17px;
    color: var(--ink);
  }
  .contact__group { margin: 0 0 16px; }
  .contact__line { margin: 0; white-space: nowrap; }
  .contact__label { color: var(--accent); }

  .person {
    position: absolute;
    right: 30px;
    top: 186px;
    text-align: right;
    font-family: "Source Sans 3", "Myriad Pro", sans-serif;
    color: var(--ink);
  }
  .person__name {
    margin: 0 0 3px;
    font-weight: 600;
    font-size: 16px;
    line-height: 20px;
    color: var(--accent);
  }
  .person__role {
    margin: 0;
    font-size: 12px;
    line-height: 16px;
    white-space: nowrap;
  }
</style>
</head>
<body>
<main class="canvas">

  <section class="card card--front" aria-label="Business card front">
    <span class="brand__dot"></span>
    <div class="brand">
      <h1 class="brand__name">KD LORN Lawyers &amp; Notary</h1>
      <p class="brand__slogan">Every Matter Handled with Steady Care</p>
    </div>
  </section>

  <section class="card card--back" aria-label="Business card back">
    <svg class="wave" viewBox="0 0 594 342" aria-hidden="true">
      <path d="M0 70 C120 110 300 60 430 90 C500 105 560 80 594 60 L594 0 L0 0 Z" fill="var(--wave)"/>
    </svg>
    <span class="brand__dot"></span>
    <div class="brand">
      <h2 class="brand__name">KD LORN Lawyers &amp; Notary</h2>
      <p class="brand__slogan">Every Matter Handled with Steady Care</p>
    </div>
    <address class="contact">
      <div class="contact__group">
        <p class="contact__line"><span class="contact__label">Office Address</span> 24/6 Tolvern Road Marleigh QLD 4287 Australia</p>
        <p class="contact__line"><span class="contact__label">Postal Address</span> P O Box 61 Marleigh QLD 4287 Australia</p>
      </div>
      <div class="contact__group">
        <p class="contact__line"><span class="contact__label">Telephone</span> 1300 274 563</p>
        <p class="contact__line"><span class="contact__label">International Telephone</span>&nbsp; +617 3956 2740</p>
      </div>
      <div class="contact__group">
        <p class="contact__line"><span class="contact__label">Facsimile</span> 1300 274 569</p>
        <p class="contact__line"><span class="contact__label">International Facsimile</span>&nbsp; +617 3871 6025</p>
      </div>
      <div class="contact__group">
        <p class="contact__line"><span class="contact__label">Email</span> clara.bexley@kdlornlegal.example</p>
        <p class="contact__line"><span class="contact__label">Web</span> www.kdlornlegal.example</p>
      </div>
    </address>
    <div class="person">
      <p class="person__name">Clara Bexley</p>
      <p class="person__role">Solicitor</p>
      <p class="person__role">Notary Public (Qld &amp; Vic)</p>
      <p class="person__role">Migration Agent</p>
      <p class="person__role">LLB, LLM,</p>
      <p class="person__role">Grad Dip in LP, Grad Dip in NP</p>
      <p class="person__role">RMA 0853162</p>
    </div>
  </section>

</main>
</body>
</html>
```